Q-Rolls Business Card

We are a modern retail clothing store. Established in 1994. I need a presentable card that will amaze vendors when given to them.

Front: Logo in middle
Info Side:

Name: Tomas Velder
Cell: 630-812-4463
Work: 630-917-3384 EXT. 417
Email: Tomas@q-rolls-example.com
Website: www.Q-rolls-example.com

Industry/Entity Type

Business

```html
<!DOCTYPE html>
<html lang="en">
<head>
<meta charset="utf-8">
<title>Q-Rolls Business Card</title>
<link href="https://fonts.googleapis.com/css2?family=Open+Sans:wght@400;600;700;800&display=swap" rel="stylesheet">
<style>
  :root {
    --stage: #2b2b2b;
    --card-black: #050505;
    --card-white: #ffffff;
    --accent-grey: #9a9a9a;
    --rule-grey: #6e6e6e;
    --ink-light: #ffffff;
  }
  * { box-sizing: border-box; margin: 0; padding: 0; }
  html, body { width: 1200px; height: 900px; overflow: hidden; }
  body {
    background: var(--stage);
    font-family: "Open Sans", Arial, sans-serif;
    color: var(--ink-light);
    position: relative;
  }
  .card {
    position: absolute;
    left: 320px;
    width: 560px;
    height: 320px;
    border-radius: 20px;
    overflow: hidden;
  }
  .card-front { top: 100px; background: var(--card-black); }
  .card-back { top: 480px; background: var(--card-white); }

  .front-wordmark {
    position: absolute;
    top: 82px; left: 0; right: 0;
    text-align: center;
    font-weight: 800;
    font-size: 82px;
    letter-spacing: 2px;
    line-height: 1;
  }
  .front-rule {
    position: absolute;
    height: 1px;
    background: var(--rule-grey);
  }
  .front-rule.top-rule { top: 72px; left: 300px; right: 24px; }
  .front-rule.bottom-rule { top: 262px; left: 24px; right: 300px; }
  .front-web {
    position: absolute;
    top: 212px; left: 0; right: 0;
    text-align: center;
    font-size: 13px;
    letter-spacing: 0.5px;
  }
  .front-web strong { font-weight: 700; }

  .back-shape { position: absolute; inset: 0; }
  .back-logo {
    position: absolute;
    left: 34px; top: 110px;
  }
  .back-wordmark {
    font-weight: 800;
    font-size: 58px;
    letter-spacing: 1px;
    line-height: 1;
  }
  .back-tagline {
    font-size: 15px;
    font-weight: 600;
    margin-top: 4px;
    letter-spacing: 0.5px;
  }
  .contact {
    position: absolute;
    right: 34px; top: 118px;
    text-align: right;
  }
  .contact-name {
    font-weight: 700;
    font-size: 17px;
    letter-spacing: 0.5px;
    margin-bottom: 4px;
    margin-right: 20px;
  }
  .contact-line {
    display: flex;
    justify-content: flex-end;
    align-items: center;
    gap: 7px;
    font-size: 12.5px;
    line-height: 19px;
  }
  .contact-line svg { width: 11px; height: 11px; flex: none; }
</style>
</head>
<body>

  <section class="card card-front" aria-label="Card front">
    <div class="front-rule top-rule"></div>
    <div class="front-wordmark">Q-ROLLS</div>
    <div class="front-web">www.<strong>Q-rolls</strong>-example.com</div>
    <div class="front-rule bottom-rule"></div>
  </section>

  <section class="card card-back" aria-label="Card back">
    <svg class="back-shape" viewBox="0 0 560 320" preserveAspectRatio="none">
      <path d="M0,0 L320,0 C430,8 520,60 560,140 L560,320 L240,320 C130,312 40,262 0,180 Z" fill="var(--accent-grey)"/>
      <path d="M0,0 L300,0 C420,10 510,64 548,150 L560,170 L560,320 L260,320 C140,310 50,260 0,168 Z" fill="var(--card-black)"/>
    </svg>

    <div class="back-logo">
      <div class="back-wordmark">Q-ROLLS</div>
      <div class="back-tagline">Established in 1994</div>
    </div>

    <div class="contact">
      <div class="contact-name">TOMAS VELDER</div>
      <div class="contact-line">630-812-4463
        <svg viewBox="0 0 12 12"><rect x="3" y="0.5" width="6" height="11" rx="1.2" fill="none" stroke="#fff" stroke-width="1.2"/><circle cx="6" cy="9.5" r="0.7" fill="#fff"/></svg>
      </div>
      <div class="contact-line">630-917-3384 EXT. 417
        <svg viewBox="0 0 12 12"><path d="M2.5 1 L4.5 1 L5.3 3.6 L4 4.6 C4.7 6.2 5.8 7.3 7.4 8 L8.4 6.7 L11 7.5 L11 9.5 C11 10.3 10.3 11 9.5 11 C5 11 1 7 1 2.5 C1 1.7 1.7 1 2.5 1 Z" fill="#fff"/></svg>
      </div>
      <div class="contact-line">Tomas@q-rolls-example.com
        <svg viewBox="0 0 12 12"><rect x="0.8" y="2.3" width="10.4" height="7.4" rx="1" fill="none" stroke="#fff" stroke-width="1.1"/><path d="M1 2.8 L6 6.6 L11 2.8" fill="none" stroke="#fff" stroke-width="1.1"/></svg>
      </div>
      <div class="contact-line">www.Q-rolls-example.com
        <svg viewBox="0 0 12 12"><circle cx="6" cy="6" r="5" fill="none" stroke="#fff" stroke-width="1.1"/><ellipse cx="6" cy="6" rx="2.2" ry="5" fill="none" stroke="#fff" stroke-width="0.9"/><path d="M1 6 H11" stroke="#fff" stroke-width="0.9"/></svg>
      </div>
    </div>
  </section>

</body>
</html>
```